Business card for law firm

Need business card for new law firm. Think confident, authoritative, conservative, but not stuffy or old-fashioned.

Contact Information for Business Card

Content for card - logo (uploaded), plus the following:

Paul Wexbury (larger font)
Managing Partner (larger font, but not as large as name)
Level 9, 41 Tansy Lane
Sydney NSW 2000
Main Tel 02 7346 2190
Direct Tel 02 6273 4415
Email paul@qvlegal.com.au
www.qvlegal.com.au

Letterhead design should include logo plus:
Level 9, 41 Tansy Lane
Sydney NSW 2000
Tel 02 6273 4415
www.qvlegal.com.au

```html
<!DOCTYPE html>
<html lang="en">
<head>
<meta charset="utf-8">
<title>Quillvale Lawyers — Business Cards</title>
<link href="https://fonts.googleapis.com/css2?family=Roboto:wght@400;500&display=swap" rel="stylesheet">
<style>
  :root {
    --backdrop: #b4b4b4;
    --card: #f7f7f6;
    --navy: #0d1b5c;
    --ink: #111318;
    --photo-light: #efefee;
    --photo-mid: #d9d7d5;
    --photo-dark: #b9b3ae;
  }
  * { margin: 0; padding: 0; box-sizing: border-box; }
  html, body { width: 1200px; height: 1200px; overflow: hidden; }
  body {
    background: var(--backdrop);
    font-family: "Roboto", Arial, sans-serif;
    position: relative;
  }
  .card {
    position: absolute;
    background: var(--card);
    overflow: hidden;
  }
  .card--front-a { left: 35px;  top: 319px; width: 586px; height: 351px; z-index: 2; }
  .card--back-a  { left: 610px; top: 363px; width: 553px; height: 331px; z-index: 1; }
  .card--back-b  { left: 35px;  top: 730px; width: 584px; height: 350px; }
  .card--front-b { left: 610px; top: 780px; width: 553px; height: 326px; }

  .photo-area {
    position: absolute; inset: 0;
    background:
      radial-gradient(ellipse 45% 40% at 58% 62%, var(--photo-mid) 0%, transparent 70%),
      radial-gradient(ellipse 30% 25% at 52% 72%, var(--photo-dark) 0%, transparent 75%),
      linear-gradient(180deg, var(--photo-light) 0%, #e6e5e3 60%, #f1f1f0 100%);
    opacity: 0.9;
  }

  .rule { position: absolute; background: var(--navy); }
  .rule--h { height: 2.5px; }
  .rule--v { width: 2.5px; }

  .brand {
    position: absolute;
    display: flex; flex-direction: column; align-items: center; gap: 10px;
    transform: translateX(-50%);
  }
  .brand__mark { width: 30px; height: 30px; background: var(--navy); }
  .brand__name {
    color: var(--navy);
    font-weight: 400;
    font-size: 17px;
    letter-spacing: 2px;
    white-space: nowrap;
  }
  .brand--small .brand__mark { width: 24px; height: 24px; }
  .brand--small .brand__name { font-size: 14px; letter-spacing: 1.5px; }

  .holder { position: absolute; color: var(--navy); text-transform: uppercase; }
  .holder__name { font-weight: 500; font-size: 25px; line-height: 1; }
  .holder__title { font-weight: 400; font-size: 16px; line-height: 1.1; margin-top: 1px; }

  .contact {
    position: absolute;
    text-align: right;
    color: var(--ink);
    font-size: 14.5px;
    line-height: 1.3;
  }
  .contact__line { position: absolute; right: 0; white-space: nowrap; }
</style>
</head>
<body>

  <!-- Front A -->
  <section class="card card--front-a">
    <div class="photo-area" role="img" aria-label="Faint photograph of a wooden judge's gavel resting on its sound block"></div>
    <div class="rule rule--h" style="left:52px; top:52px; width:331px;"></div>
    <div class="brand" style="left:468px; top:60px;">
      <div class="brand__mark"></div>
      <div class="brand__name">QUILLVALE LAWYERS</div>
    </div>
    <div class="rule rule--v" style="left:531px; top:167px; height:132px;"></div>
  </section>

  <!-- Back A -->
  <section class="card card--back-a">
    <div class="holder" style="left:37px; top:34px;">
      <div class="holder__name">Paul Wexbury</div>
      <div class="holder__title">Managing Partner</div>
    </div>
    <div class="rule rule--h" style="left:269px; top:38px; width:246px;"></div>
    <div class="rule rule--v" style="left:38px; top:146px; height:147px;"></div>
    <div class="brand brand--small" style="left:277px; top:140px;">
      <div class="brand__mark"></div>
      <div class="brand__name">QUILLVALE LAWYERS</div>
    </div>
    <div class="contact" style="right:35px; top:0; height:100%; width:260px;">
      <span class="contact__line" style="top:186px; font-size:15.5px;">PAUL WEXBURY</span>
      <span class="contact__line" style="top:213px;">02 6273 4415</span>
      <span class="contact__line" style="top:237px;">www.qvlegal.com.au</span>
      <span class="contact__line" style="top:261px;">Level 9, 41 Tansy Lane</span>
      <span class="contact__line" style="top:280px;">Sydney NSW 2000</span>
    </div>
  </section>

  <!-- Back B -->
  <section class="card card--back-b">
    <div class="holder" style="left:38px; top:35px;">
      <div class="holder__name">Paul Wexbury</div>
      <div class="holder__title">Managing Partner</div>
    </div>
    <div class="rule rule--h" style="left:283px; top:41px; width:262px;"></div>
    <div class="rule rule--v" style="left:543px; top:41px; height:116px;"></div>
    <div class="contact" style="right:38px; top:0; height:100%; width:260px;">
      <span class="contact__line" style="top:197px; font-size:15.5px;">PAUL WEXBURY</span>
      <span class="contact__line" style="top:225px;">02 6273 4415</span>
      <span class="contact__line" style="top:250px;">www.qvlegal.com.au</span>
      <span class="contact__line" style="top:276px;">Level 9, 41 Tansy Lane</span>
      <span class="contact__line" style="top:295px;">Sydney NSW 2000</span>
    </div>
    <div class="brand brand--small" style="left:110px; top:238px;">
      <div class="brand__mark"></div>
      <div class="brand__name">QUILLVALE LAWYERS</div>
    </div>
    <div class="rule rule--h" style="left:39px; top:307px; width:286px;"></div>
  </section>

  <!-- Front B -->
  <section class="card card--front-b">
    <div class="photo-area" role="img" aria-label="Faint photograph of a wooden judge's gavel resting on its sound block"></div>
    <div class="rule rule--h" style="left:272px; top:35px; width:246px;"></div>
    <div class="rule rule--v" style="left:38px; top:144px; height:144px;"></div>
    <div class="rule rule--h" style="left:38px; top:285px; width:246px;"></div>
    <div class="brand" style="left:277px; top:122px;">
      <div class="brand__mark"></div>
      <div class="brand__name">QUILLVALE LAWYERS</div>
    </div>
  </section>

</body>
</html>
```